Radiant Harvest Gathering 2021

I am looking to create a flyer for a one day prayer retreat our church is organizing. This flyer will be posted on social media, websites, mobile apps, and will also be printed so it can be mailed to people.

I am looking for something professional, with good use of our logo and band colors (logo colors).

I am counting on the designer's skill, creativity, art and knowledge of media communication to produce a flyer that will effectively and quickly convey the message we are trying to spread.

CONTENT OF THE FLYER:
Event title: Radiant Harvest Gathering
Date: Tuesday July 2nd, 2021
Time: 11:00AM - 7:00PM
Bellmore Hotel, 4817 Wexley Avenue, Portland, Maine 04109 (Room: Tamarind)
Event Key words to highlight what the event is about: Prayer, Fasting, Worship, Prophecy, Revival.
Key phrases:
A one day prayer retreat.
Jesus Chris is Lord

Contact info:
www.quvello.org
Phone: 207 555 0148
Email: contact@brookmeadow.org

```html
<!DOCTYPE html>
<html lang="en">
<head>
<meta charset="utf-8">
<title>Radiant Harvest Gathering 2021</title>
<link href="https://fonts.googleapis.com/css2?family=Great+Vibes&family=Montserrat:wght@400;600;800;900&family=Cinzel:wght@500;700&display=swap" rel="stylesheet">
<style>
  :root{
    --page:#e9e9e9;
    --ink:#0b0b0c;
    --white:#ffffff;
    --orange:#f28c1b;
    --orange-deep:#d96a0c;
    --muted:#bdbdbd;
    --glow:#6a3410;
  }
  *{box-sizing:border-box;margin:0;padding:0}
  html,body{width:736px;height:1200px;overflow:hidden;background:var(--page)}
  .flyer{
    position:absolute;left:18px;top:100px;width:700px;height:1000px;
    background:var(--ink);color:var(--white);
    font-family:'Montserrat',sans-serif;overflow:hidden;
  }
  .title{position:absolute;left:0;top:30px;width:100%;text-align:center}
  .title-script{font-family:'Great Vibes',cursive;font-size:66px;line-height:1;color:var(--white);margin-right:60px}
  .title-main{font-weight:900;font-size:104px;line-height:.95;color:var(--orange);letter-spacing:2px}
  .title-sub{font-weight:600;font-size:30px;letter-spacing:12px;margin-top:6px}
  .dove{position:absolute;right:60px;top:40px;width:120px;height:90px;border-radius:50%;
    background:radial-gradient(circle,#f2f2f2 0%,#9a9a9a 55%,transparent 72%)}
  .tagline{position:absolute;top:268px;width:100%;text-align:center;font-family:'Cinzel',serif}
  .tagline-main{font-size:32px;font-weight:500;letter-spacing:1px}
  .tagline-accent{font-size:30px;font-weight:700;color:var(--orange);margin-top:2px}
  .details{position:absolute;top:370px;left:40px;right:40px;display:flex;align-items:center;gap:18px}
  .date{display:flex;align-items:center;gap:10px}
  .date-text{font-weight:800;font-size:44px;line-height:1.05}
  .date-year{background:var(--orange);color:var(--ink);font-weight:800;font-size:22px;
    writing-mode:vertical-rl;transform:rotate(180deg);padding:8px 4px;letter-spacing:2px}
  .divider{width:2px;height:96px;background:var(--muted)}
  .info{display:flex;flex-direction:column;gap:10px;font-size:14px}
  .info-row{display:flex;align-items:flex-start;gap:10px}
  .info-row svg{flex:none;margin-top:1px}
  .time{font-size:24px;font-weight:700}
  .place{line-height:1.35}
  .keywords{position:absolute;top:500px;left:40px;right:40px;height:36px;background:var(--orange);
    color:var(--ink);font-weight:700;font-size:17px;display:flex;align-items:center;justify-content:center;letter-spacing:.5px}
  .photo{position:absolute;top:550px;left:0;width:100%;height:330px;
    background:radial-gradient(ellipse at 48% 40%,#ffd27a 0%,#c3621a 10%,var(--glow) 30%,#1a0d06 62%,var(--ink) 85%)}
  .footer{position:absolute;bottom:28px;left:36px;right:36px;display:flex;align-items:center;gap:22px;font-size:15px}
  .brand{display:flex;align-items:center;gap:8px;font-weight:800;font-size:26px;letter-spacing:1px}
  .brand-dot{width:14px;height:14px;border-radius:50%;background:var(--orange)}
  .footer-rule{width:2px;height:50px;background:var(--orange)}
  .contact{display:flex;flex-direction:column;gap:4px;flex:1}
  .contact span::before,.phone::before{content:"";display:inline-block;width:7px;height:7px;border-radius:50%;background:var(--orange);margin-right:8px;vertical-align:middle}
</style>
</head>
<body>
<main class="flyer">
  <div class="dove" role="img" aria-label="White dove in flight"></div>
  <header class="title">
    <div class="title-script">Radiant</div>
    <div class="title-main">HARVEST</div>
    <div class="title-sub">GATHERING</div>
  </header>
  <section class="tagline">
    <div class="tagline-main">A ONE DAY PRAYER RETREAT.</div>
    <div class="tagline-accent">JESUS CHRIS IS LORD</div>
  </section>
  <section class="details">
    <div class="date">
      <div class="date-text">TUESDAY<br>JULY 2ND</div>
      <div class="date-year">2021</div>
    </div>
    <div class="divider"></div>
    <div class="info">
      <div class="info-row">
        <svg width="24" height="24" viewBox="0 0 24 24"><circle cx="12" cy="12" r="10" fill="none" stroke="#f28c1b" stroke-width="2"/><path d="M12 6v6l4 3" fill="none" stroke="#f28c1b" stroke-width="2"/></svg>
        <span class="time">11:00AM - 7:00PM</span>
      </div>
      <div class="info-row">
        <svg width="24" height="24" viewBox="0 0 24 24"><path d="M12 2a7 7 0 0 0-7 7c0 5 7 13 7 13s7-8 7-13a7 7 0 0 0-7-7z" fill="#f28c1b"/><circle cx="12" cy="9" r="2.6" fill="#0b0b0c"/></svg>
        <span class="place">Bellmore Hotel, 4817 Wexley Avenue,<br>Portland, Maine 04109<br>(Room: Tamarind)</span>
      </div>
    </div>
  </section>
  <div class="keywords">#Prayer | #Fasting | #Worship | #Prophecy | #Revival</div>
  <div class="photo" role="img" aria-label="Praying hands over an open bible lit by a candle"></div>
  <footer class="footer">
    <div class="brand"><span class="brand-dot"></span>QUVELLO</div>
    <div class="footer-rule"></div>
    <div class="contact">
      <span>www.quvello.org</span>
      <span>contact@brookmeadow.org</span>
    </div>
    <div class="phone">207 555 0148</div>
  </footer>
</main>
</body>
</html>
```